Restoration Specialist in need of business card designs

One side of the business card is a bathroom ripped out down to the studs with just a sink and toilet and then the other side is the bathroom (same sink and toilet) but put back together. Like a before and after on each side behind our information. Stand out, hard to forget, business cards for my restoration company. I want a unique concept all together.
Must include in no particular order:
our business name "Summit Renewals"
Possible Logo for a restoration company
Owner; Dennis Moravec
410-386-7294
dmoravec@summitrenewalsqx.example
SummitRenewalsQX.example (our company website) BUT I am open to any and all designs and options.

Target Market(s)

Customers, Men in the mitigation, plumbing, electrical, HVAC, Roofing, insurance companies

Industry/Entity Type

Restoration/ construction

Contact Information for Business Card

Must include in no particular order: our business name "Summit Renewals" Owner; Dennis Moravec 410-386-7294 dmoravec@summitrenewalsqx.example SummitRenewalsQX.example (our company website) MAY include a list of our services: Residential~ Emergency Response ~ Board- up~ Complete Restoration

Font styles to use
Serif

Colors
0054AA
0677BA
7BADD7
CADEEF
E8F1F8
F0912C
F2A743
F7CA91
FBE8D2
FDF5EE

Requirements
Must have
• unique, memorable, not something men have seen over and over again,
Nice to have
• eye catching
Should not have
• Been something I could have made by myself

```html
<!DOCTYPE html>
<html lang="en">
<head>
<meta charset="utf-8">
<title>Summit Renewals – Business Cards</title>
<link rel="stylesheet" href="https://fonts.googleapis.com/css2?family=Tinos:wght@400;700&display=swap">
<style>
  :root {
    --backdrop: #2b2b2d;
    --card-navy: #11263b;
    --accent-orange: #ef7a1a;
    --text-white: #ffffff;
    --rule-white: rgba(255,255,255,0.9);
  }
  * { box-sizing: border-box; margin: 0; padding: 0; }
  html, body {
    width: 1200px; height: 880px; overflow: hidden;
    background: var(--backdrop);
    font-family: "Tinos", "Times New Roman", serif;
  }
  .canvas { position: relative; width: 1200px; height: 880px; }

  .card {
    position: absolute;
    width: 680px; height: 390px;
    background: var(--card-navy);
    border-radius: 26px;
    overflow: hidden;
    color: var(--text-white);
    box-shadow: 0 18px 40px rgba(0,0,0,0.45);
  }

  /* Services side */
  .card--services { left: 60px; top: 40px; text-align: center; }
  .card--services .brand-name {
    position: absolute; left: 0; right: 0; top: 92px;
    font-size: 64px; font-weight: 700; line-height: 1;
    color: var(--text-white);
  }
  .card--services .brand-rule {
    position: absolute; left: 190px; right: 190px; top: 176px;
    height: 4px; background: var(--rule-white);
  }
  .services-title {
    position: absolute; left: 0; right: 0; top: 212px;
    font-size: 22px; font-weight: 700; letter-spacing: 0.5px;
    color: var(--accent-orange);
  }
  .services-list {
    position: absolute; left: 60px; right: 60px; top: 246px;
    font-size: 21px; line-height: 1.35;
  }

  /* Contact side */
  .card--contact { left: 460px; top: 450px; }
  .card--contact .brand-name {
    position: absolute; right: 56px; top: 70px;
    font-size: 44px; font-weight: 700; line-height: 1;
    color: var(--text-white);
  }
  .owner-name {
    position: absolute; left: 60px; top: 152px;
    font-size: 30px; font-weight: 700; line-height: 1.1;
    color: var(--accent-orange);
  }
  .owner-role {
    position: absolute; left: 60px; top: 194px;
    font-size: 21px; line-height: 1.2;
  }
  .divider {
    position: absolute; left: 134px; right: 36px; top: 207px;
    height: 2px; background: var(--rule-white);
  }
  .side-tick {
    position: absolute; left: 28px; top: 164px;
    width: 8px; height: 58px; background: var(--text-white);
  }
  .contact-list {
    position: absolute; left: 60px; top: 244px;
    list-style: none; font-size: 21px;
  }
  .contact-list li { display: flex; align-items: center; gap: 14px; height: 34px; }
  .contact-list svg { width: 22px; height: 22px; fill: var(--accent-orange); }
  .website {
    position: absolute; right: 40px; top: 220px;
    font-size: 20px; line-height: 1.2;
  }
  .edge-band { position: absolute; bottom: 0; height: 22px; }
  .edge-band--orange { left: 0; width: 430px; background: var(--accent-orange); }
  .edge-band--white { left: 430px; right: 0; background: var(--text-white); }
</style>
</head>
<body>
<main class="canvas">

  <section class="card card--services" aria-label="Business card, services side">
    <div class="brand-name">Summit Renewals</div>
    <div class="brand-rule"></div>
    <h2 class="services-title">OUR SERVICES</h2>
    <p class="services-list">Residential • Emergency Response • Board- up<br>• Storm Protection • Complete Restoration</p>
  </section>

  <section class="card card--contact" aria-label="Business card, contact side">
    <div class="brand-name">Summit Renewals</div>
    <div class="side-tick"></div>
    <h1 class="owner-name">Dennis Moravec</h1>
    <p class="owner-role">Owner</p>
    <div class="divider"></div>
    <ul class="contact-list">
      <li>
        <svg viewBox="0 0 24 24" aria-hidden="true"><path d="M6.6 10.8a15.1 15.1 0 0 0 6.6 6.6l2.2-2.2a1 1 0 0 1 1-.25 11.4 11.4 0 0 0 3.6.57 1 1 0 0 1 1 1V20a1 1 0 0 1-1 1A17 17 0 0 1 3 4a1 1 0 0 1 1-1h3.5a1 1 0 0 1 1 1c0 1.25.2 2.45.57 3.57a1 1 0 0 1-.25 1z"/></svg>
        <span>410-386-7294</span>
      </li>
      <li>
        <svg viewBox="0 0 24 24" aria-hidden="true"><path d="M2 6.5l10 7.5 10-7.5V19H2z"/><path d="M2 5h20l-10 7.5z"/></svg>
        <span>dmoravec@summitrenewalsqx.example</span>
      </li>
    </ul>
    <p class="website">SummitRenewalsQX.example</p>
    <div class="edge-band edge-band--orange"></div>
    <div class="edge-band edge-band--white"></div>
  </section>

</main>
</body>
</html>
```